Business Cards that are elegant and wow

I want to create and print business cards that represent my brand and stand out from the rest. We want to ensure they stay in our branding and the integrity is not lost. I am happy to look at different shapes like square etc.

It will be printed on very thick cards and will be stylish .

I want to create and print business cards that represent my brand and stand out from the rest. We want to ensure they stay in ur branding and the integrity is not lost. I am happy to look at different shapes like square etc.

Target Market(s)

real estate professionals

Industry/Entity Type

Real Estate

Contact Information for Business Card

Maren Holt
hello@brightfernrealty.com.au
brightfernrealty.com.au
0487 316 252 (SMS)

Colors

Designer to choose colors to be used in the design.

Requirements
Must have
• My logo
• email
• website
• Name
Nice to have
• I like the idea of printing with foil or spot gloss. You want it to stand out in a sea.
Should not have
• I would like you to stay in my colour themes. Don't change the colour of my logo

```html
<!DOCTYPE html>
<html lang="en">
<head>
<meta charset="utf-8">
<title>Bright Fern Realty – Business Cards</title>
<link rel="stylesheet" href="https://fonts.googleapis.com/css2?family=Kanit:wght@500&family=Roboto:wght@400&display=swap">
<style>
  :root {
    --backdrop: #242424;
    --card-dark: #151515;
    --card-light: #efefef;
    --silver: #a3a3a3;
    --brand-blue: #1a8fd8;
    --brand-pink: #e0266f;
    --ink: #333333;
  }
  html, body {
    margin: 0;
    padding: 0;
    width: 1200px;
    height: 748px;
    overflow: hidden;
    background: var(--backdrop);
  }
  .canvas {
    position: relative;
    width: 1200px;
    height: 748px;
  }
  .card {
    position: absolute;
    width: 325px;
    height: 325px;
    border-radius: 16px;
    box-sizing: border-box;
  }
  .card-front {
    left: 220px;
    top: 204px;
    background: var(--card-dark);
    border-bottom: 2px solid var(--brand-pink);
  }
  .front-mark {
    position: absolute;
    left: 74px;
    top: 74px;
    width: 176px;
    height: 176px;
    border: 4px solid var(--silver);
    border-radius: 50%;
    box-sizing: border-box;
    display: flex;
    align-items: center;
    justify-content: center;
    text-align: center;
  }
  .front-name {
    font-family: "Kanit", sans-serif;
    font-weight: 500;
    font-size: 24px;
    line-height: 1.1;
    letter-spacing: 1px;
    color: var(--silver);
    text-transform: uppercase;
  }
  .card-back {
    left: 654px;
    top: 202px;
    background: var(--card-light);
    border-bottom: 2px solid var(--brand-pink);
  }
  .brand {
    position: absolute;
    left: 30px;
    top: 42px;
    display: flex;
    align-items: center;
    gap: 12px;
  }
  .brand-circle {
    width: 56px;
    height: 56px;
    border: 4px solid var(--brand-blue);
    border-radius: 50%;
    box-sizing: border-box;
    flex: none;
  }
  .brand-name {
    font-family: "Kanit", sans-serif;
    font-weight: 500;
    font-size: 22px;
    line-height: 1;
    color: var(--brand-blue);
    text-transform: uppercase;
    white-space: nowrap;
  }
  .person-name {
    position: absolute;
    left: 30px;
    top: 192px;
    margin: 0;
    font-family: "Kanit", sans-serif;
    font-weight: 500;
    font-size: 23px;
    color: var(--brand-blue);
  }
  .contact-list {
    position: absolute;
    left: 30px;
    top: 234px;
    margin: 0;
    padding: 0;
    list-style: none;
    font-family: "Roboto", sans-serif;
    font-size: 13.6px;
    color: var(--ink);
  }
  .contact-list li {
    display: flex;
    align-items: center;
    height: 20.5px;
  }
  .contact-icon {
    width: 12px;
    height: 12px;
    margin-right: 12px;
    flex: none;
  }
</style>
</head>
<body>
<main class="canvas">
  <section class="card card-front" aria-label="Card front">
    <div class="front-mark">
      <span class="front-name">Bright<br>Fern<br>Realty</span>
    </div>
  </section>

  <section class="card card-back" aria-label="Card back">
    <div class="brand">
      <span class="brand-circle"></span>
      <span class="brand-name">Bright Fern Realty</span>
    </div>

    <h1 class="person-name">Maren Holt</h1>

    <ul class="contact-list">
      <li>
        <svg class="contact-icon" viewBox="0 0 12 12" aria-hidden="true">
          <path d="M1 4.5 C1 2 11 2 11 4.5 L9 5.5 L8.5 4 L3.5 4 L3 5.5 Z" fill="var(--brand-blue)"/>
          <rect x="2.5" y="6" width="7" height="5" rx="1" fill="var(--brand-blue)"/>
        </svg>
        0487 316 252 (SMS)
      </li>
      <li>
        <svg class="contact-icon" viewBox="0 0 12 12" aria-hidden="true">
          <rect x="0.5" y="2" width="11" height="8" fill="var(--brand-blue)"/>
          <path d="M0.5 2 L6 6.5 L11.5 2 M0.5 10 L4.5 5.5 M11.5 10 L7.5 5.5" stroke="#fff" stroke-width="1" fill="none"/>
        </svg>
        hello@brightfernrealty.com.au
      </li>
      <li>
        <svg class="contact-icon" viewBox="0 0 12 12" aria-hidden="true">
          <circle cx="6" cy="6" r="5.5" fill="var(--brand-blue)"/>
          <path d="M0.5 6 H11.5 M6 0.5 V11.5 M6 0.5 C3 3 3 9 6 11.5 M6 0.5 C9 3 9 9 6 11.5" stroke="#fff" stroke-width="0.8" fill="none"/>
        </svg>
        www.brightfernrealty.com.au
      </li>
    </ul>
  </section>
</main>
</body>
</html>
```